I need a website for my moving company Brisk Haulers LLC. I would like the following text included in my website. I have purchased the domain briskhaulersco.example from nametrellis.example. I am not familiar with SEO or other techniques that help my page on search engines but would like the website to be optimized for Scoutly search engine. I have attached our logo below and would like it to be used in the design. The colors in the logo can be used also in the design.
Home/About Us
At Brisk Haulers LLC, we know moving. It can be difficult, stressful, and a real pain in the backside. But it doesn’t have to be! When you partner with Brisk, you get the benefits of a professional moving team that is licensed and insured for your protection along with years of experience and a dedication to providing the highest quality service, each and every time.
Our Services
We do a wide variety of local moves, including apartments, single-family homes, retirement communities, dorms, condos, and many more! Our movers are trained to protect your belongings and your home – all pieces of furniture are padded and stretch wrapped free of charge, ensuring your items and home are damage-free at the end of your move. Having added stress about packing up your home prior to moving? We’ve got you covered with our full service packing and unpacking services, too.
What You Get
When you partner with BRISK, you’ll get the best service in the industry, as well as:
* The Use of Packing & Moving Materials: The hourly rate includes the use of our dollies, ratchet straps, pads, moving tools, and property protection like floor mats, door-jamb protectors, stairwell protectors, and plenty of muscle!
• Trained, Licensed, and Insured Movers: All of our movers are highly trained to provide you with the best service, and to ensure the protection of you and your items.
• Professional: Honest, Uniformed, Nice, Knowledgeable Service is what you’ll get with every member of our moving teams.
• Custom Service for Every Move: Every move is as unique as the person or business moving. Our training and equipment allows us to customize every project to ensure the very best for every client.
Target Market(s)
Home and Business movers
Industry/Entity Type
Moving Company
Colors
Designer to choose colors to be used in the design.
Requirements
Must have
- 2 sides
Nice to have
- Colorful design with logo included.
Should not have
- animated characters

```html
<!DOCTYPE html>
<html lang="en">
<head>
<meta charset="utf-8">
<title>Brisk Haulers LLC – Moving Company</title>
<link href="https://fonts.googleapis.com/css2?family=Oswald:wght@400;500;700&family=Lato:wght@400;700&display=swap" rel="stylesheet">
<style>
:root{
  --orange:#f7821b;
  --orange-dark:#ee6c0c;
  --green:#8cc63f;
  --green-dark:#76ad2c;
  --ink:#2b2b2b;
  --text:#555;
  --muted:#888;
  --grey:#e9e9e9;
  --line:#d5d5d5;
  --dark:#2e2e2e;
  --white:#fff;
  --box:#d9a565;
  --box-dark:#b97a3c;
  --cream:#f3e6d2;
}
*{margin:0;padding:0;box-sizing:border-box}
html,body{width:1200px;height:4627px;overflow:hidden}
body{font-family:'Lato',Arial,sans-serif;color:var(--text);background:var(--white);position:relative}
.abs{position:absolute}
h2{font-family:'Oswald',Arial,sans-serif;font-weight:500;color:var(--ink);letter-spacing:1px}
.btn{display:inline-block;background:var(--green);color:var(--white);font-family:'Lato',sans-serif;font-weight:700;border-radius:4px;text-align:center}

/* top bar */
.topbar{top:0;left:0;width:1200px;height:28px;background:var(--dark);color:#ddd;font-size:13px}
.topbar .mail{left:122px;top:6px}
.topbar .phone{left:557px;top:6px}
.social{display:flex;gap:8px}
.social span{width:17px;height:17px;border-radius:50%;background:#bbb;display:block}
.topbar .social{right:120px;top:5px}

/* header + hero */
.hero{top:28px;left:0;width:1200px;height:675px;
  background:
    radial-gradient(ellipse 260px 300px at 1100px 250px,rgba(92,140,52,.75),rgba(92,140,52,0) 70%),
    radial-gradient(ellipse 120px 140px at 210px 470px,rgba(110,150,60,.6),rgba(110,150,60,0) 70%),
    radial-gradient(ellipse 300px 240px at 600px 380px,rgba(250,244,232,.95),rgba(250,244,232,0) 75%),
    radial-gradient(ellipse 240px 300px at 90px 520px,rgba(201,140,75,.9),rgba(201,140,75,0) 75%),
    radial-gradient(ellipse 240px 260px at 1090px 580px,rgba(196,135,70,.85),rgba(196,135,70,0) 75%),
    radial-gradient(ellipse 320px 140px at 600px 620px,rgba(150,120,90,.45),rgba(150,120,90,0) 75%),
    linear-gradient(180deg,#f7efe3 0%,#ecdcc3 55%,#d8b88e 100%)}
.header{top:28px;left:0;width:1200px;height:127px;background:linear-gradient(to bottom,rgba(255,255,255,.97),rgba(255,255,255,.6))}
.logo{display:flex;align-items:center;gap:10px;font-family:'Lato',sans-serif;font-weight:700;color:var(--orange);font-size:30px}
.logo i{width:30px;height:30px;background:var(--orange);display:block}
.header .logo{left:122px;top:55px}
.nav{right:320px;top:68px;display:flex;gap:24px;font-size:15px;color:var(--ink)}
.nav .active{color:var(--orange);border-bottom:2px solid var(--orange);padding-bottom:4px}
.header .quote-btn{right:120px;top:62px;padding:7px 16px;font-size:14px}
.hero-copy{top:410px;left:0;width:1200px;text-align:center;color:var(--white)}
.hero-copy h1{font-family:'Oswald',sans-serif;font-weight:700;font-size:36px;letter-spacing:1px;text-shadow:0 2px 6px rgba(0,0,0,.55)}
.hero-copy p{font-size:14px;line-height:20px;margin-top:4px;text-shadow:0 1px 4px rgba(0,0,0,.7)}
.hero-copy .btn{margin-top:22px;padding:10px 26px;font-size:15px}
.arrow{width:40px;height:40px}
.dots{top:655px;left:585px;display:flex;gap:8px}
.dots span{width:9px;height:9px;border-radius:50%;background:rgba(255,255,255,.6)}
.dots span.on{background:var(--white)}

/* quote */
.quote{top:703px;left:0;width:1200px;height:201px;background:var(--grey)}
.quote h2{position:absolute;top:20px;width:100%;text-align:center;font-size:22px}
.field{position:absolute;height:40px;background:var(--white);border:1px solid var(--line);font-size:12px;color:var(--muted);padding:12px 14px 0 34px}
.field svg{position:absolute;left:12px;top:13px}
.quote .send{position:absolute;left:608px;top:122px;width:472px;height:40px;line-height:40px;font-size:14px;border-radius:0}

/* about */
.about{top:904px;left:0;width:1200px;height:432px}
.about h2{position:absolute;left:120px;top:78px;font-size:30px}
.about p{position:absolute;left:120px;top:134px;width:470px;font-size:14px;line-height:21px}
.about .btn{position:absolute;left:120px;top:266px;padding:8px 22px;font-size:14px}
.about .mover{left:694px;top:34px;width:232px;height:398px;
  background:
    radial-gradient(ellipse 90px 70px at 110px 260px,rgba(222,160,90,1),rgba(222,160,90,0) 80%),
    radial-gradient(ellipse 70px 130px at 116px 170px,rgba(80,98,72,.9),rgba(80,98,72,0) 80%),
    radial-gradient(ellipse 40px 40px at 116px 60px,rgba(200,160,130,.8),rgba(200,160,130,0) 80%),
    radial-gradient(ellipse 60px 110px at 116px 360px,rgba(90,90,95,.6),rgba(90,90,95,0) 80%),
    linear-gradient(180deg,#fbfaf7,#f2ede5)}

/* services */
.services{top:1336px;left:0;width:1200px;height:537px;background:var(--orange)}
.services h2{position:absolute;top:38px;width:100%;text-align:center;color:var(--white);font-size:30px}
.svc{position:absolute;width:455px;height:168px;background:var(--white);box-shadow:0 3px 6px rgba(0,0,0,.15)}
.svc .ico{position:absolute;left:22px;top:22px;width:64px;height:64px;background:var(--green);display:flex;align-items:center;justify-content:center}
.svc h3{position:absolute;left:100px;top:24px;font-size:16px;color:var(--ink);font-weight:700}
.svc p{position:absolute;left:100px;top:52px;width:330px;font-size:13px;line-height:20px}

/* what you get */
.get{top:1873px;left:0;width:1200px;height:867px}
.squares{left:108px;top:76px;display:flex;gap:6px}
.squares span{width:24px;height:24px;display:block}
.get h2{position:absolute;top:80px;width:100%;text-align:center;font-size:32px}
.get .lead{position:absolute;top:126px;width:100%;text-align:center;font-size:14px;color:var(--ink)}
.tile{position:absolute;width:456px;height:212px}
.tile-badge{position:absolute;width:50px;height:50px;border-radius:50%;background:var(--white);display:flex;align-items:center;justify-content:center;box-shadow:0 1px 3px rgba(0,0,0,.15)}
.perk{position:absolute;width:456px;font-size:13px;line-height:19px;color:var(--ink)}
.t1{background:radial-gradient(ellipse 140px 90px at 330px 110px,#f6c98a,rgba(246,201,138,0) 80%),radial-gradient(ellipse 160px 110px at 120px 140px,#c98a45,rgba(201,138,69,0) 80%),linear-gradient(135deg,#b9772f,#e0a35a 55%,#a8652a)}
.t2{background:radial-gradient(ellipse 120px 110px at 120px 120px,#d96b3a,rgba(217,107,58,0) 80%),radial-gradient(ellipse 120px 110px at 340px 120px,#d96b3a,rgba(217,107,58,0) 80%),radial-gradient(ellipse 120px 60px at 230px 150px,#f4d9b0,rgba(244,217,176,0) 80%),linear-gradient(135deg,#f1c48a,#e6a867)}
.t3{background:radial-gradient(ellipse 150px 100px at 220px 130px,#f1c271,rgba(241,194,113,0) 80%),radial-gradient(ellipse 140px 120px at 90px 60px,#8a5a35,rgba(138,90,53,0) 80%),linear-gradient(135deg,#c88945,#e3ae62 50%,#b07535)}
.t4{background:radial-gradient(ellipse 170px 80px at 230px 140px,#f2ebd8,rgba(242,235,216,0) 80%),radial-gradient(ellipse 90px 80px at 60px 60px,#f6e2b8,rgba(246,226,184,0) 80%),linear-gradient(135deg,#f08f3a,#f6a24a 50%,#e3792a)}

/* booking */
.book{top:2740px;left:0;width:1200px;height:354px;background:
  radial-gradient(ellipse 600px 140px at 250px 90px,rgba(255,190,120,.55),rgba(255,190,120,0) 75%),
  radial-gradient(ellipse 500px 140px at 950px 290px,rgba(230,95,10,.6),rgba(230,95,10,0) 75%),
  linear-gradient(160deg,#f99a3a 0%,var(--orange) 40%,var(--orange-dark) 100%)}
.book-card{left:435px;top:46px;width:407px;height:259px;background:var(--white);box-shadow:0 4px 10px rgba(0,0,0,.2);text-align:center}
.book-card h2{margin-top:42px;font-size:26px;font-weight:400}
.book-card .rule{width:260px;height:1px;background:var(--line);margin:16px auto 0}
.book-card .slot{width:220px;margin:14px auto 0;border:1px solid var(--line);padding:10px 0 12px}
.slot b{display:block;font-size:13px;font-weight:400;color:var(--ink)}
.slot small{display:block;font-size:11px;color:var(--muted);margin-top:3px}
.slot .btn{margin-top:10px;width:130px;padding:6px 0;font-size:13px}

/* testimonials */
.clients{top:3094px;left:0;width:1200px;height:485px}
.clients h2{position:absolute;top:44px;width:100%;text-align:center;font-size:30px}
.client{position:absolute;top:114px;width:284px;height:309px;text-align:center}
.client.featured{border:3px solid var(--green);box-shadow:0 2px 8px rgba(0,0,0,.12)}
.client .avatar{width:90px;height:90px;border-radius:50%;margin:30px auto 0}
.client h4{margin-top:20px;font-size:14px;color:var(--ink)}
.client .role{font-size:11px;color:var(--muted);margin-top:4px}
.client p{font-size:11px;line-height:17px;width:210px;margin:12px auto 0}
.client .more{font-size:11px;font-weight:700;color:var(--ink);margin-top:6px}
.clients .view{position:absolute;left:540px;top:462px;width:123px;padding:7px 0;font-size:14px}

/* newsletter */
.news{top:3579px;left:0;width:1200px;height:293px}
.news h2{position:absolute;top:76px;width:100%;text-align:center;font-size:30px;font-weight:700}
.news .sub{position:absolute;top:118px;width:100%;text-align:center;font-size:15px;letter-spacing:2px;color:var(--ink)}
.news .email{left:324px;top:166px;width:432px;height:26px;border:1px solid var(--line);font-size:11px;color:var(--muted);padding:6px 10px}
.news .submit{left:756px;top:166px;width:86px;height:26px;line-height:26px;font-size:12px;border-radius:0}

/* map */
.map{top:3872px;left:0;width:1200px;height:339px;background:
  radial-gradient(ellipse 500px 200px at 300px 120px,#f3efe8,rgba(243,239,232,0) 75%),
  radial-gradient(ellipse 300px 260px at 820px 200px,#ece7dc,rgba(236,231,220,0) 75%),
  radial-gradient(ellipse 200px 120px at 1000px 280px,#dfe6d2,rgba(223,230,210,0) 75%),
  radial-gradient(ellipse 220px 140px at 120px 300px,#e0e6d4,rgba(224,230,212,0) 75%),
  linear-gradient(135deg,#efebe3,#e6e0d5)}
.directions{left:55px;top:12px;padding:9px 18px;font-size:13px;border-radius:2px}
.zoom{left:8px;width:26px;height:26px;background:var(--white);border:1px solid var(--line);text-align:center;font-size:18px;line-height:24px;color:var(--ink)}
.pin{left:588px;top:140px}

/* footer */
.footer{top:4211px;left:0;width:1200px;height:361px;background:var(--orange);color:var(--white)}
.footer .logo{position:absolute;left:122px;top:100px;color:var(--white);font-size:28px}
.footer .logo i{background:var(--white)}
.footer .about-f{position:absolute;left:122px;top:164px;width:230px;font-size:14px;line-height:21px}
.footer h5{position:absolute;top:88px;font-size:15px;letter-spacing:1px}
.footer ul{position:absolute;top:124px;list-style:none;font-size:14px;line-height:22px}
.footer ul li::before{content:"› ";}
.addr{position:absolute;left:654px;top:124px;font-size:13px;line-height:22px}
.addr div{display:flex;align-items:center;gap:8px}
.addr span.d{width:10px;height:10px;border-radius:50%;background:rgba(255,255,255,.85);display:block}
.gallery{position:absolute;left:866px;top:124px;display:grid;grid-template-columns:repeat(3,50px);grid-auto-rows:50px;gap:4px}
.gallery div{background:linear-gradient(135deg,#f4d7ad,#c98f4f)}
.gallery div:nth-child(2n){background:linear-gradient(135deg,#e9b87a,#a9703a)}

.bottom{top:4572px;left:0;width:1200px;height:55px;background:var(--dark);color:var(--white);font-size:14px}
.bottom .legal{left:122px;top:18px;font-weight:700}
.bottom .social{right:120px;top:18px}
</style>
</head>
<body>

<div class="abs topbar">
  <span class="abs mail">info@briskhaulersco.example</span>
  <span class="abs phone">(555) 014-2290</span>
  <div class="abs social"><span></span><span></span><span></span><span></span><span></span></div>
</div>

<div class="abs hero" role="img" aria-label="Photo of a smiling couple on a sofa surrounded by moving boxes and plants"></div>
<div class="abs header">
  <div class="abs logo"><i></i>BRISK HAULERS</div>
  <nav class="abs nav">
    <span class="active">Home</span><span>About</span><span>Services</span><span>What You Get</span><span>Testimonail</span><span>Contact</span>
  </nav>
  <span class="abs btn quote-btn">Get A Quote</span>
</div>
<div class="abs hero-copy">
  <h1>BRISK HAULERS LLC</h1>
  <p>Lorem Ipsum is simply dummy text of the printing<br>and typesetting industry.</p>
  <span class="btn">Book Today</span>
</div>
<svg class="abs arrow" style="left:30px;top:375px" viewBox="0 0 40 40"><path d="M25 8 13 20l12 12" fill="none" stroke="#fff" stroke-width="4"/></svg>
<svg class="abs arrow" style="right:30px;top:375px" viewBox="0 0 40 40"><path d="M15 8l12 12-12 12" fill="none" stroke="#fff" stroke-width="4"/></svg>
<div class="abs dots"><span class="on"></span><span></span><span></span></div>

<section class="abs quote">
  <h2>GET A QUOTE</h2>
  <div class="field" style="left:120px;top:62px;width:230px"><svg width="12" height="12" viewBox="0 0 12 12"><circle cx="6" cy="4" r="3" fill="#999"/><path d="M0 12a6 5 0 0 1 12 0z" fill="#999"/></svg>Name</div>
  <div class="field" style="left:362px;top:62px;width:230px"><svg width="12" height="12" viewBox="0 0 12 12"><rect x="0" y="2" width="12" height="8" fill="none" stroke="#999" stroke-width="1.5"/><path d="M0 2l6 5 6-5" fill="none" stroke="#999" stroke-width="1.5"/></svg>E-mail</div>
  <div class="field" style="left:604px;top:62px;width:230px"><svg width="12" height="12" viewBox="0 0 12 12"><path d="M2 1h3l1 3-2 1a7 7 0 0 0 3 3l1-2 3 1v3c-6 1-10-3-9-9z" fill="#999"/></svg>Phone</div>
  <div class="field" style="left:846px;top:62px;width:234px"><svg width="12" height="12" viewBox="0 0 12 12"><path d="M6 0a4 4 0 0 1 4 4c0 3-4 8-4 8S2 7 2 4a4 4 0 0 1 4-4z" fill="#999"/><circle cx="6" cy="4" r="1.5" fill="#fff"/></svg>Location</div>
  <div class="field" style="left:120px;top:122px;width:472px"><svg width="12" height="12" viewBox="0 0 12 12"><path d="M1 1h10v10H1z M3 4h6M3 6h6M3 8h4" fill="none" stroke="#999" stroke-width="1.2"/></svg>Description</div>
  <span class="btn send">SEND REQUEST</span>
</section>

<section class="abs about">
  <h2>ABOUT US</h2>
  <p>At Brisk Haulers LLC, we know moving. It can be difficult, stressful, and a real pain in the backside. But it doesn't have to be! When you partner with Brisk, you get the benefits of a professional moving team that is licensed and insured for your protection along with years of experience and a dedication to providing the highest quality service, each and every time.</p>
  <span class="btn">Read More</span>
  <div class="abs mover" role="img" aria-label="Photo of a uniformed mover in a cap carrying a branded cardboard box"></div>
</section>

<section class="abs services">
  <h2>OUR SERVICES</h2>
  <svg class="abs arrow" style="left:45px;top:165px" viewBox="0 0 40 40"><path d="M25 8 13 20l12 12" fill="none" stroke="#fff" stroke-width="4"/></svg>
  <svg class="abs arrow" style="right:45px;top:165px" viewBox="0 0 40 40"><path d="M15 8l12 12-12 12" fill="none" stroke="#fff" stroke-width="4"/></svg>

  <article class="svc" style="left:117px;top:108px">
    <div class="ico"><svg width="38" height="38" viewBox="0 0 38 38"><rect x="4" y="10" width="8" height="14" fill="none" stroke="#fff" stroke-width="2.5"/><path d="M12 30h20M12 6v24" stroke="#fff" stroke-width="2.5"/><circle cx="14" cy="31" r="3" fill="#fff"/></svg></div>
    <h3>Local Moves</h3>
    <p>Lorem Ipsum is simply dummy text of the printing and typesetting industry. Lorem Ipsum has been the industry's standard dummy text ever since the 1500s.</p>
  </article>
  <article class="svc" style="left:626px;top:108px">
    <div class="ico"><svg width="38" height="38" viewBox="0 0 38 38"><rect x="8" y="4" width="22" height="30" fill="#fff"/><g fill="#8cc63f"><rect x="12" y="8" width="4" height="4"/><rect x="22" y="8" width="4" height="4"/><rect x="12" y="16" width="4" height="4"/><rect x="22" y="16" width="4" height="4"/><rect x="16" y="26" width="6" height="8"/></g></svg></div>
    <h3>Including Apartments</h3>
    <p>Lorem Ipsum is simply dummy text of the printing and typesetting industry. Lorem Ipsum has been the industry's standard dummy text ever since the 1500s.</p>
  </article>
  <article class="svc" style="left:117px;top:321px">
    <div class="ico"><svg width="38" height="38" viewBox="0 0 38 38"><path d="M4 18 19 5l15 13" fill="none" stroke="#fff" stroke-width="3"/><rect x="9" y="17" width="20" height="16" fill="#fff"/><rect x="16" y="24" width="6" height="9" fill="#8cc63f"/></svg></div>
    <h3>Single-Family Homes</h3>
    <p>Lorem Ipsum is simply dummy text of the printing and typesetting industry. Lorem Ipsum has been the industry's standard dummy text ever since the 1500s.</p>
  </article>
  <article class="svc" style="left:626px;top:321px">
    <div class="ico"><svg width="38" height="38" viewBox="0 0 38 38"><path d="M3 15 19 5l16 10" fill="none" stroke="#fff" stroke-width="3"/><rect x="7" y="15" width="24" height="18" fill="#fff"/><rect x="11" y="19" width="5" height="5" fill="#8cc63f"/><rect x="22" y="19" width="5" height="5" fill="#8cc63f"/><rect x="16" y="26" width="6" height="7" fill="#8cc63f"/></svg></div>
    <h3>Dorms</h3>
    <p>Lorem Ipsum is simply dummy text of the printing and typesetting industry. Lorem Ipsum has been the industry's standard dummy text ever since the 1500s.</p>
  </article>
</section>

<section class="abs get">
  <div class="abs squares"><span style="background:#8cc63f"></span><span style="background:#a8d46a"></span><span style="background:#f7821b"></span><span style="background:#f99a3a"></span><span style="background:#ee6c0c"></span></div>
  <h2>WHAT YOU GET</h2>
  <p class="lead">When you partner with BRISK, you'll get the best service in the industry, as well as:</p>

  <div class="tile t1" style="left:117px;top:175px" role="img" aria-label="Photo of stacked cardboard moving boxes"></div>
  <div class="tile-badge" style="left:316px;top:362px"><svg width="24" height="24" viewBox="0 0 24 24"><path d="M3 8l9-4 9 4v10l-9 4-9-4z" fill="none" stroke="#8cc63f" stroke-width="2"/></svg></div>
  <p class="perk" style="left:117px;top:418px"><b>The Use of Packing &amp; Moving Materials:</b> The hourly rate includes the use of our dollies, ratchet straps, pads, moving tools, and property protection like floor mats, door-jamb protectors, stairwell protectors, and plenty of muscle!</p>

  <div class="tile t2" style="left:626px;top:175px" role="img" aria-label="Photo of two movers carrying furniture"></div>
  <div class="tile-badge" style="left:827px;top:362px"><svg width="24" height="24" viewBox="0 0 24 24"><rect x="6" y="3" width="12" height="18" rx="2" fill="none" stroke="#8cc63f" stroke-width="2"/><path d="M9 12l2 2 4-4" fill="none" stroke="#8cc63f" stroke-width="2"/></svg></div>
  <p class="perk" style="left:626px;top:418px"><b>Trained, Licensed, and Insured Movers:</b> All of our movers are highly trained to provide you with the best service, and to ensure the protection of you and your items.</p>

  <div class="tile t3" style="left:117px;top:512px" role="img" aria-label="Photo of a mover packing belongings"></div>
  <div class="tile-badge" style="left:316px;top:699px"><svg width="24" height="24" viewBox="0 0 24 24"><circle cx="12" cy="8" r="4" fill="#8cc63f"/><path d="M4 21a8 7 0 0 1 16 0z" fill="#8cc63f"/></svg></div>
  <p class="perk" style="left:117px;top:755px"><b>Professional:</b> Honest, Uniformed, Nice, Knowledgeable Service is what you'll get with every member of our moving teams.</p>

  <div class="tile t4" style="left:626px;top:512px" role="img" aria-label="Photo of a family relaxing among moving boxes in a new home"></div>
  <div class="tile-badge" style="left:827px;top:699px"><svg width="24" height="24" viewBox="0 0 24 24"><path d="M3 11 12 3l9 8v10H3z" fill="none" stroke="#8cc63f" stroke-width="2"/></svg></div>
  <p class="perk" style="left:626px;top:755px"><b>Custom Service for Every Move:</b> Every move is as unique as the person or business moving. Our training and equipment allows us to customize every project to ensure the very best for every client.</p>
</section>

<section class="abs book">
  <div class="abs book-card">
    <h2>BOOK AN APPOINMENT</h2>
    <div class="rule"></div>
    <div class="slot">
      <b>Moving Service</b>
      <small>1 hour · $125.00</small>
      <span class="btn">BOOK</span>
    </div>
  </div>
</section>

<section class="abs clients">
  <h2>CLIENT SAY</h2>
  <div class="client" style="left:105px">
    <div class="avatar" style="background:radial-gradient(circle at 50% 40%,#f0d6b8,#c79a6c 70%,#a07248)" role="img" aria-label="Portrait of client Jane Doe"></div>
    <h4>Jane Doe</h4><div class="role">Engineer of Media Production</div>
    <p>Lorem Ipsum is simply dummy text of the printing and typesetting industry. Lorem Ipsum is simply dummy.</p>
    <div class="more">Read More →</div>
  </div>
  <div class="client featured" style="left:466px">
    <div class="avatar" style="background:radial-gradient(circle at 50% 40%,#d9c6b3,#8c7767 70%,#5a4a40)" role="img" aria-label="Portrait of client Jane Dolor"></div>
    <h4>Jane Dolor</h4><div class="role">Engineer of Media Production</div>
    <p>Lorem Ipsum is simply dummy text of the printing and typesetting industry. Lorem Ipsum is simply dummy.</p>
    <div class="more">Read More →</div>
  </div>
  <div class="client" style="left:833px">
    <div class="avatar" style="background:radial-gradient(circle at 50% 40%,#e2c6ad,#80675a 70%,#4a3c34)" role="img" aria-label="Portrait of client John Doe"></div>
    <h4>John Doe</h4><div class="role">Engineer of Media Production</div>
    <p>Lorem Ipsum is simply dummy text of the printing and typesetting industry. Lorem Ipsum is simply dummy.</p>
    <div class="more">Read More →</div>
  </div>
  <span class="btn view">View More</span>
</section>

<section class="abs news">
  <h2>SUBSCRIBE TO OUR NEWSLETTER</h2>
  <p class="sub">TO RECEIVE THE LATEST NEWS &amp; UPDATE</p>
  <div class="abs email">Your Email</div>
  <span class="abs btn submit">SUBMIT</span>
</section>

<section class="abs map" role="img" aria-label="Street map showing the company location with a marker">
  <span class="abs btn directions">➤ GET DIRECTIONS</span>
  <div class="abs zoom" style="top:12px">+</div>
  <div class="abs zoom" style="top:40px">−</div>
  <svg class="abs pin" width="24" height="34" viewBox="0 0 24 34"><path d="M12 0a12 12 0 0 1 12 12c0 9-12 22-12 22S0 21 0 12A12 12 0 0 1 12 0z" fill="#4a7fb5"/><circle cx="12" cy="12" r="4.5" fill="#fff"/></svg>
</section>

<footer class="abs footer">
  <div class="logo"><i></i>BRISK HAULERS</div>
  <p class="about-f">Lorem Ipsum is simply dummy text of the printing and types etting ind Lorem Ipsu m been the industry's …<br><b>Read More →</b></p>
  <h5 style="left:423px">QUICK LINKS</h5>
  <ul style="left:423px"><li>Home</li><li>About</li><li>Services</li><li>What You Get</li><li>Testimonail</li><li>Contact</li></ul>
  <h5 style="left:654px">ADDRESS</h5>
  <div class="addr">
    <div><span class="d"></span>412 Elmwood Ave, Springdale,</div>
    <div style="padding-left:18px">ST 00000</div>
    <div><span class="d"></span>(555) 014-2290</div>
    <div><span class="d"></span>(555) 014-2290</div>
    <div><span class="d"></span>info@briskhaulersco.example</div>
    <div><span class="d"></span>Mon-Sat 9:00am-6:00pm</div>
  </div>
  <h5 style="left:866px">GALLERY</h5>
  <div class="gallery" role="img" aria-label="Gallery of moving job photos"><div></div><div></div><div></div><div></div><div></div><div></div></div>
</footer>

<div class="abs bottom">
  <span class="abs legal">Privacy policy · Legal mentions · Terms and Conditions</span>
  <div class="abs social"><span></span><span></span><span></span><span></span><span></span></div>
</div>

</body>
</html>
```